Cobalt Ridge Goods Co.
Cobalt Ridge Goods Co. business cards - Miscellaneous
Cobalt Ridge Goods Co. business cards
Professional
Trevor Kasmund
President
Denver | Colorado | USA
trev@cobaltridgegoods.example
www.cobaltridgegoods.example
I would like the logo to be on the front of the business card preferably the size of the height of the card on the left side
I would like the logo to be on the back of the business card as well. The logo should take up the entire back of the business card.
quartzfen quartzfen
Kindly do some star rating... it will really help us to make stationary for your like designs.. thanks!
kasmundtk kasmundtk
We are also looking for at stationary options. Please provide any options for letterhead, etc..

```html
<!DOCTYPE html>
<html lang="en">
<head>
<meta charset="utf-8">
<title>Cobalt Ridge Goods Co. — Business Cards</title>
<link rel="stylesheet" href="https://fonts.googleapis.com/css2?family=Tinos:wght@400;700&display=swap">
<style>
  :root {
    --navy: #27267d;
    --navy-deep: #1f1e6a;
    --red: #e3262c;
    --yellow: #f3d320;
    --grey-text: #6d6d72;
    --card-white: #ffffff;
    --stage: #f1f1f3;
  }
  * { box-sizing: border-box; margin: 0; padding: 0; }
  html, body { width: 1200px; height: 778px; overflow: hidden; }
  body {
    background: var(--stage);
    font-family: "Tinos", "Times New Roman", serif;
    position: relative;
  }
  .card {
    position: absolute;
    top: 246px;
    width: 500px;
    height: 286px;
    border-radius: 14px;
    overflow: hidden;
    box-shadow: 0 6px 18px rgba(0,0,0,0.15);
  }
  .card--front { left: 60px; background: var(--card-white); }
  .card--back { left: 640px; background: var(--navy); }

  .front-wave { position: absolute; left: 0; bottom: 0; width: 500px; height: 286px; }

  .holder { position: absolute; left: 0; top: 46px; width: 250px; }
  .holder__name { padding-left: 74px; font-size: 24px; color: var(--navy); line-height: 1; }
  .holder__title { padding-left: 140px; margin-top: 4px; font-size: 11px; color: var(--grey-text); }
  .holder__rule { margin-top: 4px; height: 2px; background: var(--yellow); width: 240px; }

  .location { position: absolute; left: 98px; top: 126px; font-size: 12px; color: var(--grey-text); }

  .contacts { position: absolute; right: 262px; top: 152px; list-style: none; text-align: right; }
  .contacts li {
    display: flex; align-items: center; justify-content: flex-end;
    gap: 5px; font-size: 11.5px; color: var(--grey-text); line-height: 17px;
  }
  .contacts svg { width: 10px; height: 10px; fill: var(--navy); }

  .brand-block {
    position: absolute; right: 34px; top: 26px; width: 170px; height: 176px;
    border: 3px solid var(--navy);
    display: flex; flex-direction: column; justify-content: center; align-items: center;
    text-align: center; color: var(--navy); font-weight: 700;
    font-size: 30px; line-height: 1.02; text-transform: uppercase;
  }

  .back-ridge {
    position: absolute; left: 0; bottom: 0; width: 500px; height: 110px;
    background: linear-gradient(180deg, rgba(255,255,255,0) 0%, rgba(255,255,255,0.08) 100%);
  }
  .back-brand {
    position: absolute; left: 26px; top: 34px; width: 190px; height: 218px;
    border: 3px solid var(--card-white);
    display: flex; flex-direction: column; justify-content: center; align-items: center;
    text-align: center; color: var(--card-white); font-weight: 700;
    font-size: 34px; line-height: 1.02; text-transform: uppercase;
  }
  .back-web {
    position: absolute; left: 246px; top: 128px;
    font-size: 14px; color: var(--yellow);
  }
</style>
</head>
<body>

  <section class="card card--front" aria-label="Business card front">
    <svg class="front-wave" viewBox="0 0 500 286" aria-hidden="true">
      <path d="M0,236 C120,214 220,262 330,244 C410,231 460,208 500,198 L500,286 L0,286 Z" fill="var(--navy)"/>
      <path d="M0,228 C120,206 220,254 330,236 C410,223 460,200 500,190" fill="none" stroke="var(--red)" stroke-width="6"/>
      <path d="M0,235 C120,213 220,261 330,243 C410,230 460,207 500,197" fill="none" stroke="var(--card-white)" stroke-width="4"/>
    </svg>

    <div class="holder">
      <p class="holder__name">Trevor Kasmund</p>
      <p class="holder__title">President</p>
      <div class="holder__rule"></div>
    </div>

    <p class="location">Denver | Colorado | USA</p>

    <ul class="contacts">
      <li><svg viewBox="0 0 10 10"><rect x="2.5" y="0.5" width="5" height="9" rx="1"/></svg>720.555.0148</li>
      <li><svg viewBox="0 0 10 10"><rect x="0.5" y="2" width="9" height="6"/></svg>trev@cobaltridgegoods.example</li>
      <li><svg viewBox="0 0 10 10"><circle cx="5" cy="5" r="4.5"/></svg>www.cobaltridgegoods.example</li>
    </ul>

    <div class="brand-block">
      <span>Cobalt</span><span>Ridge</span><span>Goods Co.</span>
    </div>
  </section>

  <section class="card card--back" aria-label="Business card back">
    <div class="back-ridge" role="img" aria-label="Faint mountain ridge illustration"></div>
    <div class="back-brand">
      <span>Cobalt</span><span>Ridge</span><span>Goods Co.</span>
    </div>
    <p class="back-web">www.cobaltridgegoods.example</p>
  </section>

</body>
</html>
```